Start up business website

IT Support provider that caters towards law enforcement / police departments. We'll offer remote IT support, backup / recovery services and cyber security. Will add updates soon.

Target Market(s)

Police departments / Law Enforcement

Coding

Coded - Design and coding required

Number of Pages Required

5+ page

Font styles to use
Other font styles liked:
• Use font style in uploaded logo

Colors
0054AA
0677BA
7BADD7
CADEEF
E8F1F8

```html
<!DOCTYPE html>
<html lang="en">
<head>
<meta charset="utf-8">
<title>Bastion Support Services</title>
<link href="https://fonts.googleapis.com/css2?family=Russo+One&family=Montserrat:ital,wght@0,400;0,500;0,600;0,700;1,500&display=swap" rel="stylesheet">
<style>
:root{
  --blue:#0054AA;
  --blue-mid:#0677BA;
  --blue-light:#7BADD7;
  --blue-pale:#CADEEF;
  --blue-mist:#E8F1F8;
  --navy:#0b1424;
  --ink:#333;
  --muted:#777;
  --white:#fff;
  --display:"Russo One",sans-serif;
  --body:"Montserrat",sans-serif;
}
*{margin:0;padding:0;box-sizing:border-box}
html,body{width:1200px;height:3600px;overflow:hidden;background:var(--white);font-family:var(--body);color:var(--ink)}
.page{position:relative;width:1200px;height:3600px;overflow:hidden}
.backdrop{position:absolute;left:0;top:0}
.abs{position:absolute}
.brand{font-family:var(--body);font-weight:700;color:var(--blue-mid);letter-spacing:1px}
.nav a{position:absolute;top:33px;font-size:11px;color:var(--white);text-decoration:none;letter-spacing:.5px}
.nav .current{left:607px;top:24px;width:68px;height:32px;border:2px solid var(--blue);border-radius:16px;text-align:center;line-height:28px;color:var(--blue-light)}
.display{font-family:var(--display);color:var(--blue);text-transform:uppercase;letter-spacing:1px}
.eyebrow{font-size:15px;color:var(--ink)}
.btn{position:absolute;height:40px;border-radius:20px;background:var(--blue);color:var(--white);font-family:var(--display);font-size:13px;letter-spacing:1.5px;padding-left:20px;line-height:40px}
.btn::after{content:"";position:absolute;right:5px;top:5px;width:30px;height:30px;border-radius:50%;background:var(--white)}
.btn.ghost{background:transparent;border:1.5px solid var(--white);line-height:37px}
.copy{font-size:11px;line-height:20px;color:var(--muted)}
.svc-label{font-family:var(--display);font-size:13px;color:var(--blue);letter-spacing:1px}
.svc-text{font-size:11px;line-height:20px;color:var(--white)}
.card-title{font-size:15px;font-weight:600;line-height:20px;color:var(--ink)}
.read{font-size:12px;font-weight:600;color:var(--blue);text-decoration:underline}
.date{position:absolute;width:22px;height:120px;background:var(--blue);color:var(--white);font-size:11px;writing-mode:vertical-rl;transform:rotate(180deg);text-align:center;line-height:22px}
.foot-head{font-family:var(--display);font-size:13px;color:var(--blue);letter-spacing:1px}
.foot-list{list-style:none;font-size:11px;color:var(--white)}
.foot-list li{height:22px;position:relative;padding-left:18px}
.foot-list li::before{content:"";position:absolute;left:0;top:6px;width:5px;height:5px;border-radius:50%;background:var(--blue-mid)}
.foot-text{font-size:11px;line-height:19px;color:var(--white)}
</style>
</head>
<body>
<div class="page">
<svg class="backdrop" width="1200" height="3600" viewBox="0 0 1200 3600">
  <defs>
    <linearGradient id="heroShade" x1="0" y1="0" x2="1" y2="1">
      <stop offset="0" stop-color="#0e2a5c"/><stop offset=".55" stop-color="#0a1a38"/><stop offset="1" stop-color="#050b18"/>
    </linearGradient>
    <linearGradient id="aboutShade" x1="0" y1="0" x2="1" y2="1">
      <stop offset="0" stop-color="#2a5fa8"/><stop offset="1" stop-color="#0c2550"/>
    </linearGradient>
    <linearGradient id="badgeShade" x1="0" y1="0" x2="1" y2="1">
      <stop offset="0" stop-color="#c9a53a"/><stop offset="1" stop-color="#1b2a55"/>
    </linearGradient>
    <linearGradient id="darkShade" x1="0" y1="0" x2="0" y2="1">
      <stop offset="0" stop-color="#0d1726"/><stop offset="1" stop-color="#121c2c"/>
    </linearGradient>
    <linearGradient id="personShade" x1="0" y1="0" x2="0" y2="1">
      <stop offset="0" stop-color="#3b4f70"/><stop offset="1" stop-color="#101a2c"/>
    </linearGradient>
    <linearGradient id="news1" x1="0" y1="0" x2="1" y2="1"><stop offset="0" stop-color="#6d7a54"/><stop offset="1" stop-color="#1f2530"/></linearGradient>
    <linearGradient id="news2" x1="0" y1="0" x2="1" y2="1"><stop offset="0" stop-color="#3a4654"/><stop offset="1" stop-color="#0c1118"/></linearGradient>
    <linearGradient id="news3" x1="0" y1="0" x2="1" y2="1"><stop offset="0" stop-color="#2c3f8a"/><stop offset="1" stop-color="#10131f"/></linearGradient>
  </defs>

  <!-- hero -->
  <g role="img" aria-label="Photo of analysts working at monitors in a security operations room">
    <path d="M0 0H1200V505Q900 695 600 700Q300 695 0 505Z" fill="url(#heroShade)"/>
  </g>
  <path d="M0 505Q300 695 600 700Q900 695 1200 505" fill="none" stroke="#b9bec6" stroke-width="5"/>
  <rect x="0" y="0" width="1200" height="82" fill="rgba(4,10,24,.8)"/>
  <circle cx="58" cy="305" r="20" fill="none" stroke="var(--blue)" stroke-width="2"/>
  <path d="M62 297l-8 8 8 8" fill="none" stroke="#fff" stroke-width="2"/>
  <circle cx="1142" cy="305" r="20" fill="none" stroke="var(--blue)" stroke-width="2"/>
  <path d="M1138 297l8 8-8 8" fill="none" stroke="#fff" stroke-width="2"/>
  <circle cx="975" cy="40" r="20" fill="var(--blue)"/>
  <path d="M967 32c2-2 4 0 5 3s-2 3-1 5 3 4 5 5 2-3 5-1 2 4 0 5c-6 3-17-8-14-17z" fill="#fff"/>
  <circle cx="600" cy="690" r="26" fill="#fff" stroke="#c3c7cd" stroke-width="3"/>
  <circle cx="600" cy="690" r="16" fill="var(--navy)"/>

  <!-- about imagery -->
  <path d="M855 776Q920 838 1034 832Q1050 1000 960 1115Q905 1175 855 1186Q805 1175 750 1115Q660 1000 676 832Q790 838 855 776Z" fill="#fff" stroke="#cfd3d8" stroke-width="3"/>
  <g role="img" aria-label="Photo of a laptop with a padlock graphic and a coffee cup">
    <path d="M855 792Q915 848 1020 844Q1032 996 950 1104Q900 1160 855 1170Q810 1160 760 1104Q678 996 690 844Q795 848 855 792Z" fill="url(#aboutShade)"/>
  </g>
  <circle cx="918" cy="1138" r="100" fill="#fff"/>
  <g role="img" aria-label="Photo of a police officer's shoulder patch">
    <circle cx="918" cy="1138" r="92" fill="url(#badgeShade)"/>
  </g>

  <!-- services -->
  <path d="M0 1290L108 1275Q340 1420 600 1235Q860 1420 1092 1275L1200 1290V1850H0Z" fill="url(#darkShade)"/>
  <circle cx="600" cy="1545" r="360" fill="none" stroke="#1c2a40" stroke-width="2"/>
  <line x1="600" y1="1683" x2="600" y2="1772" stroke="#8a96a8" stroke-width="1.5"/>
  <polyline points="390,1742 460,1742 510,1806" fill="none" stroke="#8a96a8" stroke-width="1.5"/>
  <polyline points="812,1742 740,1742 690,1806" fill="none" stroke="#8a96a8" stroke-width="1.5"/>
  <g>
    <circle cx="600" cy="1630" r="54" fill="#fff" stroke="var(--blue)" stroke-width="4"/>
    <rect x="578" y="1612" width="44" height="30" rx="3" fill="none" stroke="#222" stroke-width="2.5"/>
    <rect x="584" y="1618" width="32" height="18" fill="var(--blue-mid)"/>
    <rect x="570" y="1644" width="60" height="5" rx="2" fill="#222"/>
  </g>
  <g>
    <circle cx="337" cy="1742" r="54" fill="#fff" stroke="var(--blue)" stroke-width="4"/>
    <path d="M315 1742a22 22 0 0 1 44 0" fill="none" stroke="#222" stroke-width="3"/>
    <rect x="309" y="1738" width="9" height="16" rx="3" fill="var(--blue-mid)"/>
    <rect x="356" y="1738" width="9" height="16" rx="3" fill="var(--blue-mid)"/>
    <circle cx="337" cy="1748" r="10" fill="none" stroke="#222" stroke-width="2.5"/>
    <path d="M320 1775a17 12 0 0 1 34 0" fill="none" stroke="#222" stroke-width="2.5"/>
  </g>
  <g>
    <circle cx="865" cy="1742" r="54" fill="#fff" stroke="var(--blue)" stroke-width="4"/>
    <ellipse cx="855" cy="1720" rx="18" ry="6" fill="none" stroke="#222" stroke-width="2.5"/>
    <path d="M837 1720v42c0 4 8 7 18 7M873 1720v14" fill="none" stroke="#222" stroke-width="2.5"/>
    <path d="M837 1734c0 4 8 7 18 7M837 1748c0 4 8 7 18 7" fill="none" stroke="#222" stroke-width="2"/>
    <circle cx="879" cy="1756" r="15" fill="var(--blue-mid)" stroke="#222" stroke-width="2.5"/>
    <path d="M879 1747v9l6 4" fill="none" stroke="#fff" stroke-width="2.5"/>
  </g>

  <!-- discuss band -->
  <path d="M0 1850H1200V2212Q900 2420 600 2556Q300 2420 0 2212Z" fill="var(--blue)"/>
  <g role="img" aria-label="Photo of a businessman in a suit using a tablet">
    <path d="M470 2340Q600 2320 730 2340V2492Q665 2526 600 2556Q535 2526 470 2492Z" fill="url(#personShade)"/>
  </g>
  <circle cx="600" cy="1905" r="112" fill="#0a1830" stroke="#c9ccd2" stroke-width="10"/>
  <circle cx="600" cy="1905" r="124" fill="none" stroke="var(--blue-light)" stroke-width="2"/>
  <circle cx="510" cy="1808" r="4" fill="var(--blue-light)"/>
  <circle cx="690" cy="1808" r="4" fill="var(--blue-light)"/>
  <circle cx="600" cy="1772" r="4" fill="var(--blue-light)"/>

  <!-- news cards -->
  <g fill="#fff" stroke="#dcdfe3" stroke-width="1.5">
    <rect x="150" y="2724" width="285" height="378" rx="8"/>
    <rect x="457" y="2724" width="285" height="378" rx="8"/>
    <rect x="765" y="2724" width="285" height="378" rx="8"/>
  </g>
  <g role="img" aria-label="Photo of two police officers taking notes"><rect x="154" y="2728" width="277" height="187" fill="url(#news1)"/></g>
  <g role="img" aria-label="Photo of a hooded hacker at a laptop"><rect x="461" y="2728" width="277" height="187" fill="url(#news2)"/></g>
  <g role="img" aria-label="Photo of a police officer beside a patrol car at night"><rect x="769" y="2728" width="277" height="187" fill="url(#news3)"/></g>
  <g fill="var(--blue)">
    <path d="M241 3069h4l5 4-5 4h-4z"/><path d="M548 3069h4l5 4-5 4h-4z"/><path d="M856 3069h4l5 4-5 4h-4z"/>
  </g>

  <!-- footer -->
  <path d="M0 3290Q300 3162 600 3162Q900 3162 1200 3290V3600H0Z" fill="#0c1524"/>
  <circle cx="600" cy="3170" r="26" fill="#fff" stroke="#c3c7cd" stroke-width="3"/>
  <circle cx="600" cy="3170" r="16" fill="var(--navy)"/>
  <rect x="0" y="3555" width="1200" height="45" fill="var(--blue)"/>
  <circle cx="629" cy="3388" r="16" fill="var(--blue)"/>
  <path d="M629 3379a6 6 0 0 1 6 6c0 5-6 11-6 11s-6-6-6-11a6 6 0 0 1 6-6z" fill="none" stroke="#fff" stroke-width="2"/>
  <circle cx="629" cy="3447" r="16" fill="var(--blue)"/>
  <path d="M622 3440c2-2 3 0 4 2s-1 3 0 4 2 3 4 4 2-2 4-1 1 3 0 4c-5 2-13-6-12-13z" fill="#fff"/>
  <circle cx="629" cy="3490" r="16" fill="var(--blue)"/>
  <rect x="621" y="3484" width="16" height="11" rx="1" fill="#fff"/>
  <path d="M621 3485l8 6 8-6" fill="none" stroke="var(--blue)" stroke-width="1.5"/>
  <rect x="888" y="3408" width="250" height="36" rx="18" fill="#fff"/>
  <circle cx="140" cy="3414" r="42" fill="none" stroke="#fff" stroke-width="3"/>
</svg>

<!-- header -->
<div class="abs brand" style="left:200px;top:27px;font-size:22px;display:none"></div>
<div class="abs brand" style="left:62px;top:27px;font-size:20px">BASTION</div>
<div class="abs" style="left:62px;top:52px;font-size:8px;font-weight:700;color:var(--blue-mid);letter-spacing:1px">SUPPORT SERVICES</div>
<nav class="nav">
  <a class="current" href="#">HOME</a>
  <a href="#" style="left:694px">ABOUT</a>
  <a href="#" style="left:754px">SERVICES</a>
  <a href="#" style="left:828px">NEWS</a>
  <a href="#" style="left:879px">CONTACT</a>
</nav>
<div class="abs" style="left:1007px;top:24px;font-size:11px;color:#fff">Call Us On :</div>
<div class="abs" style="left:1007px;top:39px;font-family:var(--display);font-size:15px;color:#fff;letter-spacing:1px">555 010 2040</div>

<!-- hero -->
<div class="abs" style="left:111px;top:205px;font-size:14px;color:#fff;letter-spacing:.5px">GET HIGH QUALITY</div>
<h1 class="abs" style="left:100px;top:234px;font-family:var(--display);font-size:64px;line-height:66px;color:#fff;font-weight:400">CYBER<br>SECURITY</h1>
<div class="btn" style="left:98px;top:383px;width:190px">CONTACT US</div>

<!-- about -->
<div class="abs eyebrow" style="left:165px;top:775px">About Us</div>
<h2 class="abs display" style="left:163px;top:800px;font-size:29px;line-height:34px;font-weight:400">Bastion Support<br>Services</h2>
<p class="abs copy" style="left:163px;top:882px;width:380px">Lorem Ipsum has been the industry's standard dummy text ever since the 1500s, when an unknown printer took a galley of type and scrambled it to make a type specimen book.</p>
<p class="abs copy" style="left:163px;top:950px;width:380px">Lorem Ipsum has been the industry's standard dummy text ever since the 1500s, when an unknown printer took a galley of type and scrambled it to make a type specimen book.</p>
<p class="abs" style="left:165px;top:1025px;width:370px;font-size:13px;line-height:21px;font-style:italic;color:#444">We'll offer remote IT support, backup / recovery services and cyber security.</p>
<div class="btn" style="left:163px;top:1087px;width:180px">LEARN MORE</div>

<!-- services -->
<div class="abs" style="left:0;top:1366px;width:1200px;text-align:center;font-size:15px;color:#fff">What We Offer</div>
<h2 class="abs display" style="left:0;top:1396px;width:1200px;text-align:center;font-size:28px;line-height:34px;font-weight:400">Services We<br>Provide</h2>
<div class="abs svc-label" style="left:0;top:1497px;width:1200px;text-align:center">CYBER SECURITY</div>
<p class="abs svc-text" style="left:480px;top:1520px;width:240px;text-align:center">Lorem Ipsum has been the industry's standard dummy text evertext.</p>
<div class="abs svc-label" style="left:40px;top:1715px;width:225px;text-align:right">REMOTE IT SUPPORT</div>
<p class="abs svc-text" style="left:40px;top:1738px;width:225px;text-align:right">Lorem Ipsum has been the industry's standard dummy text evertext.</p>
<div class="abs svc-label" style="left:935px;top:1715px;width:230px">BACKUP / RECOVERY</div>
<p class="abs svc-text" style="left:935px;top:1738px;width:225px">Lorem Ipsum has been the industry's standard dummy text evertext.</p>

<!-- discuss -->
<h2 class="abs" style="left:250px;top:2100px;width:700px;text-align:center;font-size:35px;line-height:42px;font-style:italic;font-weight:500;color:#fff">Let's Discuss About How We Can Help Make Your Business More Secured.</h2>
<p class="abs" style="left:0;top:2240px;width:1200px;text-align:center;font-size:13px;color:#fff">We'll offer remote IT support, backup / recovery services and cyber security.</p>
<div class="btn ghost" style="left:504px;top:2275px;width:192px">CONTACT US</div>

<!-- news -->
<div class="abs eyebrow" style="left:0;top:2620px;width:1200px;text-align:center">Stay Upto Date</div>
<h2 class="abs display" style="left:0;top:2650px;width:1200px;text-align:center;font-size:29px;font-weight:400">Latest News</h2>
<div class="date" style="left:150px;top:2798px">09 Nov 2021</div>
<div class="date" style="left:457px;top:2798px">09 Nov 2021</div>
<div class="date" style="left:765px;top:2798px">09 Nov 2021</div>
<article class="abs" style="left:168px;top:2940px;width:250px">
  <h3 class="card-title">Lorem Ipsum has been the printi industry's standa</h3>
  <p class="copy" style="margin-top:12px">Lorem Ipsum has been the industry's standa dummy text ever since the when an unknown printer took a galley of type scramb</p>
  <div class="read" style="margin-top:12px">Read More</div>
</article>
<article class="abs" style="left:475px;top:2940px;width:250px">
  <h3 class="card-title">Lorem Ipsum has been the printi industry's standa</h3>
  <p class="copy" style="margin-top:12px">Lorem Ipsum has been the industry's standa dummy text ever since the when an unknown printer took a galley of type scramb</p>
  <div class="read" style="margin-top:12px">Read More</div>
</article>
<article class="abs" style="left:783px;top:2940px;width:250px">
  <h3 class="card-title">Lorem Ipsum has been the printi industry's standa</h3>
  <p class="copy" style="margin-top:12px">Lorem Ipsum has been the industry's standa dummy text ever since the when an unknown printer took a galley of type scramb</p>
  <div class="read" style="margin-top:12px">Read More</div>
</article>

<!-- footer -->
<div class="abs brand" style="left:196px;top:3392px;font-size:28px">BASTION</div>
<div class="abs" style="left:146px;top:3426px;font-size:11px;font-weight:700;color:var(--blue-mid);letter-spacing:1px">SUPPORT SERVICES</div>
<div class="abs" style="left:165px;top:3458px;font-size:11px;color:#fff;letter-spacing:6px">f ▶ t</div>
<div class="abs foot-head" style="left:338px;top:3318px">SITEMAP</div>
<ul class="abs foot-list" style="left:338px;top:3354px">
  <li>Home</li><li>About</li><li>Services</li><li>News</li><li>Contact</li>
</ul>
<div class="abs foot-head" style="left:614px;top:3318px">CONTACT INFO</div>
<div class="abs foot-text" style="left:661px;top:3360px;width:190px">BASTION SUPPORT SERVICES</div>
<div class="abs foot-text" style="left:661px;top:3381px;width:190px">101 - loremipsum simple text print type setting text industry</div>
<div class="abs foot-text" style="left:661px;top:3438px">+1 555 010 2040</div>
<div class="abs foot-text" style="left:661px;top:3481px">info@bastionsupport.example</div>
<div class="abs foot-head" style="left:888px;top:3318px">NEWSLETTER</div>
<div class="abs foot-text" style="left:890px;top:3360px;width:240px">Would you like to receive our exclusive update for signup Today !</div>
<div class="abs" style="left:906px;top:3419px;font-size:11px;color:#666">Enter Email *</div>
<div class="btn" style="left:888px;top:3456px;width:178px">SUBSCRIBE</div>
<div class="abs" style="left:0;top:3570px;width:1200px;text-align:center;font-size:11px;color:#fff">©BASTION SUPPORT SERVICES - 2021 Allrights reserved.</div>
</div>
</body>
</html>
```